Business Card Design

I need a Business Card that will catch the attention that will not get thrown in a Drawer. I have 23 companies I use for Auto, Home, Life, and Business Insurance. I make sure that people have the best coverage for the $ spent.

Industry/Entity Type

Business

Contact Information for Business Card

Dorlin Insurance Agency, Inc., Marcus Helgren, 4375 West Tamber Lane Corvale, Aldenia 45192 555-281-7496, www.dorlinagency.example, Facemark, Linkhub, Circleup

```html
<!DOCTYPE html>
<html lang="en">
<head>
<meta charset="utf-8">
<title>Dorlin Insurance Agency – Business Card</title>
<link rel="stylesheet" href="https://fonts.googleapis.com/css2?family=EB+Garamond:wght@400;600;700&display=swap">
<style>
  :root {
    --backdrop: #2b2b2b;
    --card-white: #ffffff;
    --card-shade: #ececec;
    --brown: #5a3411;
    --brown-dark: #4a2a0c;
    --gold: #d8901f;
  }
  * { margin: 0; padding: 0; box-sizing: border-box; }
  html, body {
    width: 1200px;
    height: 900px;
    overflow: hidden;
    background: var(--backdrop);
  }
  .canvas {
    position: relative;
    width: 1200px;
    height: 900px;
    display: flex;
    align-items: center;
    justify-content: center;
  }
  .business-card {
    position: relative;
    width: 1000px;
    height: 572px;
    background: linear-gradient(160deg, var(--card-white) 35%, var(--card-shade) 100%);
    overflow: hidden;
    font-family: "EB Garamond", Garamond, serif;
  }
  .agency-name {
    position: absolute;
    left: 70px;
    top: 46px;
    font-size: 46px;
    font-weight: 700;
    line-height: 1.2;
    color: var(--brown);
    letter-spacing: 0.01em;
    white-space: nowrap;
  }
  .social-links {
    position: absolute;
    right: 44px;
    top: 90px;
    display: flex;
    gap: 12px;
    font-size: 16px;
    font-weight: 600;
    line-height: 1.2;
    color: var(--brown);
    white-space: nowrap;
  }
  .rule {
    position: absolute;
    left: 0;
    width: 100%;
    height: 3px;
  }
  .rule--gold { top: 124px; background: var(--gold); }
  .rule--brown { top: 131px; background: var(--brown); }
  .agent-name {
    position: absolute;
    left: 70px;
    top: 180px;
    font-size: 40px;
    font-weight: 700;
    line-height: 1.2;
    color: var(--brown);
  }
  .contact {
    position: absolute;
    left: 70px;
    top: 248px;
    font-size: 30px;
    line-height: 1.3;
    color: var(--gold);
  }
  .footer-band {
    position: absolute;
    left: 0;
    bottom: 0;
    width: 100%;
    height: 186px;
    background: linear-gradient(180deg, var(--brown) 0%, var(--brown-dark) 100%);
    display: flex;
    align-items: center;
    justify-content: center;
  }
  .website {
    font-size: 30px;
    font-weight: 700;
    letter-spacing: 0.3em;
    color: var(--gold);
    white-space: nowrap;
  }
</style>
</head>
<body>
  <main class="canvas">
    <article class="business-card">
      <h1 class="agency-name">Dorlin Insurance Agency, Inc.</h1>
      <div class="social-links">
        <span>Facemark</span>
        <span>Linkhub</span>
        <span>Circleup</span>
      </div>
      <div class="rule rule--gold"></div>
      <div class="rule rule--brown"></div>
      <h2 class="agent-name">Marcus Helgren</h2>
      <p class="contact">
        4375, West Tamber Lane, Corvale, Aldenia 45192<br>
        Tel: 555-281-7496
      </p>
      <footer class="footer-band">
        <span class="website">www.dorlinagency.example</span>
      </footer>
    </article>
  </main>
</body>
</html>
```